Crimson Vantage Cleaning Solutions

Need a logo and business card design. I want to use a translucent business card. I want to abbreviate the name C.V.C.S. Commercial Cleaning, because my is Dov. I’d also like to incorporate a knight or something like that. I want the idea to tie in with the word Crimson. New ideas are welcome, i don’t want to limit anyone’s creativity.

Target Market(s)

Commercial Cleaning for businesses.

Contact Information for Business Card

Crimson
Vantage
Cleaning
Solutions

```html
<!DOCTYPE html>
<html lang="en">
<head>
<meta charset="utf-8">
<title>C.V.C.S. Commercial Cleaning – Business Card</title>
<link href="https://fonts.googleapis.com/css2?family=Lato:wght@400;700&family=Open+Sans:wght@400;600&display=swap" rel="stylesheet">
<style>
  :root {
    --backdrop: #7b4b26;
    --card-light: #dcbd8f;
    --card-mid: #c9a270;
    --card-dark: #b68752;
    --ink: #141010;
    --rule: #5c4630;
  }
  * { margin: 0; padding: 0; box-sizing: border-box; }
  html, body {
    width: 1200px; height: 900px; overflow: hidden;
    background: var(--backdrop);
  }
  .canvas { position: relative; width: 1200px; height: 900px; }
  .card {
    position: absolute;
    left: 330px;
    width: 556px;
    height: 343px;
    background: linear-gradient(160deg, var(--card-light) 0%, var(--card-mid) 50%, var(--card-dark) 100%);
    box-shadow: 2px 3px 6px rgba(0,0,0,0.35);
    color: var(--ink);
    text-align: center;
  }
  .card--back { top: 90px; }
  .card--front { top: 469px; width: 558px; }

  .person-name {
    position: absolute; left: 0; right: 0; top: 154px;
    font-family: "Lato", sans-serif; font-weight: 700; font-size: 21px;
    letter-spacing: 0.2px; line-height: 1;
  }
  .person-role {
    position: absolute; left: 0; right: 0; top: 177px;
    font-family: "Open Sans", sans-serif; font-size: 16px; line-height: 1;
  }
  .divider {
    position: absolute; left: 180px; width: 195px; height: 1px;
    background: var(--rule);
  }
  .divider--top { top: 116px; }
  .divider--bottom { top: 222px; }

  .contact-list {
    position: absolute; left: 0; right: 0; top: 128px;
    list-style: none;
    font-family: "Open Sans", sans-serif; font-size: 16px; line-height: 20px;
  }
  .contact-list strong { font-weight: 600; }
  .address {
    position: absolute; left: 0; right: 0; top: 238px;
    font-family: "Open Sans", sans-serif; font-size: 16px; line-height: 20px;
    font-style: normal;
  }

  .brand {
    position: absolute; left: 0; right: 0; top: 112px;
    font-family: "Lato", sans-serif; font-weight: 700; color: var(--ink);
  }
  .brand-name { display: block; font-size: 72px; line-height: 1; letter-spacing: 1px; }
  .brand-tagline { display: block; font-size: 20px; line-height: 1; margin-top: 12px; letter-spacing: 0.3px; }
</style>
</head>
<body>
<main class="canvas">
  <section class="card card--back" aria-label="Business card back">
    <p class="person-name" style="top:65px">MARCUS HALE</p>
    <p class="person-role" style="top:88px">Managing Director</p>
    <div class="divider divider--top"></div>
    <ul class="contact-list">
      <li><strong>P:</strong> 020-555 0147 62</li>
      <li><strong>M:</strong> 020-555 0147 62</li>
      <li><strong>E:</strong> info@cvcsclean.com</li>
      <li><strong>W:</strong> www.cvcsclean.com</li>
    </ul>
    <div class="divider divider--bottom"></div>
    <address class="address">48 Harbour Lane, Suite 3<br>Eastbridge, EB4 7QR.</address>
  </section>

  <section class="card card--front" aria-label="Business card front">
    <h1 class="brand">
      <span class="brand-name">C.V.C.S.</span>
      <span class="brand-tagline">COMMERCIAL CLEANING</span>
    </h1>
  </section>
</main>
</body>
</html>
```